Consulting/Brand Licensing business needs business card

We need a business card created for our IP company, that also does consulting and brand licensing. We would like this card to be vague, as our other business' are in the cannabis industry and this is a non-cannabis touching entity. Perhaps something that hints vaguely at the industry without alerting or possibly offending the receiver.

Target Market(s)

CEOs/Key Decision Makers/Industry Leaders

Contact Information for Business Card

No address, simply list Seattle, WA. Phone: 206-555-0147. Name: Dilan Vesterby // email: Dilan@pulvanixa.com

Colors

Designer to choose colors to be used in the design.

Requirements
Must have
• Logo, Name, Email, Phone number, "Consulting, Licensing and Branding Specialists"
Nice to have
• We would like this to be more professional than playful.

```html
<!DOCTYPE html>
<html lang="en">
<head>
<meta charset="utf-8">
<title>Pulvanixa Business Card</title>
<link href="https://fonts.googleapis.com/css2?family=Montserrat:wght@300;400;700;800&display=swap" rel="stylesheet">
<style>
  :root {
    --backdrop: #b1b1b1;
    --brand-red: #c34e30;
    --paper: #ffffff;
    --ink: #2b2b2b;
    --ink-soft: #3a3a3a;
  }
  * { margin: 0; padding: 0; box-sizing: border-box; }
  html, body {
    width: 1200px;
    height: 1200px;
    overflow: hidden;
    background: var(--backdrop);
    font-family: "Montserrat", Arial, sans-serif;
  }
  .stage {
    position: relative;
    width: 1200px;
    height: 1200px;
  }
  .card {
    position: absolute;
    left: 267px;
    width: 659px;
    height: 375px;
  }
  .card--front {
    top: 223px;
    background: var(--brand-red);
  }
  .front-lockup {
    position: absolute;
    left: 0;
    right: 0;
    top: 128px;
    text-align: center;
  }
  .wordmark {
    color: var(--paper);
    font-weight: 800;
    font-size: 56px;
    letter-spacing: 2px;
    line-height: 56px;
  }
  .legal-name {
    margin-top: 16px;
    color: var(--ink);
    font-weight: 400;
    font-size: 19px;
    line-height: 22px;
    letter-spacing: -0.3px;
  }
  .tagline {
    margin-top: 10px;
    color: var(--ink);
    font-weight: 400;
    font-size: 12px;
    line-height: 16px;
    letter-spacing: 1.6px;
    text-transform: uppercase;
  }
  .card--back {
    top: 657px;
    background: var(--paper);
  }
  .side-band {
    position: absolute;
    left: 0;
    top: 0;
    width: 203px;
    height: 100%;
    background: var(--brand-red);
  }
  .contact {
    position: absolute;
    left: 239px;
    top: 143px;
    line-height: 26px;
  }
  .contact__name {
    color: var(--brand-red);
    font-weight: 700;
    font-size: 23px;
    letter-spacing: 0.4px;
  }
  .contact__line {
    color: var(--ink-soft);
    font-weight: 300;
    font-size: 21px;
  }
</style>
</head>
<body>
  <main class="stage">
    <section class="card card--front">
      <div class="front-lockup">
        <div class="wordmark">PULVANIXA</div>
        <div class="legal-name">Pulvanixa, Inc</div>
        <div class="tagline">Consulting, Licensing and Branding Specialists</div>
      </div>
    </section>

    <section class="card card--back">
      <div class="side-band"></div>
      <div class="contact">
        <div class="contact__name">Dilan Vesterby</div>
        <div class="contact__line">Dilan@pulvanixa.com</div>
        <div class="contact__line">206-555-0147</div>
        <div class="contact__line">Seattle, WA</div>
      </div>
    </section>
  </main>
</body>
</html>
```